Etiketten für Honigwein
Zielgruppe
Wir sind eine kleine Metmanufaktur im Süden des Schwarzwalds und haben uns auf den Namen
Tarquil getauft. Bei unseren Produkten setzen wir auf Qualität statt auf Quantität. Zu unserer
Zielgruppe gehören exklusive Schlossrestaurants, Gaststätten in antikem oder mittelalterlichen
Ambiente sowie Mittelaltermärkte. Später soll diese auf Feinkostläden und auch den Getränkehandel
erweitert werden.
Aufgabenstellung
Siehe angehängtes PDF.
Falls ein Designer eine bessere Idee zu manchen Punkten oder dem gesamten Design hat, sind wir gerne bereit, uns von diesen inspirieren zu lassen.
Posivitbeispiele sind mit Positiv1, Positiv2, etc. und Negativbeispiele mit Negativ1, Negativ2, etc. beschriftet.

```html
<!DOCTYPE html>
<html lang="de">
<head>
<meta charset="utf-8">
<title>Tarquil – Etiketten für Honigwein</title>
<link rel="stylesheet" href="https://fonts.googleapis.com/css2?family=Montserrat:wght@500;700&family=Playfair+Display:ital@1&family=Cormorant+Garamond:wght@500&display=swap">
<style>
  :root {
    --paper: #ececec;
    --ink: #2b2b2b;
    --ink-soft: #5e5e5e;
    --gold: #c9a26b;
    --gold-deep: #b8844c;
    --cherry-top: #f0605a;
    --cherry-bottom: #c81e1e;
    --apple-top: #ffc9a4;
    --apple-bottom: #f4a27b;
    --capsule: #262626;
  }
  * { box-sizing: border-box; margin: 0; padding: 0; }
  html, body { width: 848px; height: 1200px; overflow: hidden; }
  body {
    position: relative;
    background: var(--paper);
    font-family: "Montserrat", sans-serif;
    color: var(--ink);
  }

  /* closure seal */
  .closure-seal {
    position: absolute; left: 121px; top: 45px;
    width: 130px; height: 130px; border-radius: 50%;
    background: var(--capsule);
    display: flex; align-items: center; justify-content: center;
  }
  .closure-seal__face {
    width: 110px; height: 110px; border-radius: 50%;
    background: #b9ad97;
    display: flex; flex-direction: column; align-items: center; justify-content: center; gap: 6px;
  }
  .closure-seal__name { font-weight: 700; font-size: 16px; letter-spacing: 1px; color: var(--ink); }
  .closure-seal__ring { width: 10px; height: 10px; border-radius: 50%; border: 1.5px solid var(--ink); }

  /* flat label panels */
  .label-panel {
    position: absolute; top: 220px; width: 207px; height: 878px;
    border-radius: 6px; overflow: hidden;
    display: flex; flex-direction: column; align-items: center;
  }
  .label-panel--cherry { left: 81px; background: linear-gradient(180deg, var(--cherry-top), var(--cherry-bottom)); }
  .label-panel--apple { left: 329px; background: linear-gradient(180deg, var(--apple-top), var(--apple-bottom)); }

  .neck-band {
    width: 100%; height: 190px; background: var(--capsule);
    display: flex; flex-direction: column; align-items: center; justify-content: flex-end;
    padding-bottom: 14px; gap: 6px;
  }
  .neck-band__name { color: var(--gold); font-weight: 700; font-size: 9px; letter-spacing: 1.5px; }
  .neck-band__ring { width: 8px; height: 8px; border-radius: 50%; border: 1px solid var(--gold); }

  .label-body { margin-top: 260px; display: flex; flex-direction: column; align-items: center; text-align: center; }
  .label-body__tagline { font-size: 6.5px; letter-spacing: 2px; color: var(--gold); text-transform: uppercase; font-weight: 500; }
  .label-body__brand { display: flex; align-items: center; gap: 6px; margin-top: 18px; }
  .label-body__name { font-weight: 700; font-size: 26px; letter-spacing: 2px; color: var(--ink); text-transform: uppercase; }
  .label-body__ring { width: 12px; height: 12px; border-radius: 50%; border: 2px solid var(--ink); }
  .label-body__met { font-weight: 700; font-size: 10px; letter-spacing: 1px; margin-top: 12px; color: var(--ink); }
  .label-body__origin { font-size: 6.5px; font-weight: 700; letter-spacing: 1px; text-transform: uppercase; margin-top: 8px; color: var(--ink); }
  .label-body__variety { font-weight: 700; font-size: 10px; letter-spacing: 3px; color: var(--gold); margin-top: 18px; }
  .label-body__year { font-family: "Playfair Display", serif; font-style: italic; font-size: 14px; color: var(--gold); margin-top: 8px; }
  .label-body__fruit { width: 40px; height: 40px; border-radius: 50%; margin-top: 44px; }
  .label-body__sweetness { font-family: "Cormorant Garamond", serif; font-size: 10px; color: var(--gold); margin-top: 22px; letter-spacing: .5px; }
  .label-panel--apple .label-body__sweetness,
  .label-panel--apple .label-body__year,
  .label-panel--apple .label-body__variety { color: var(--gold-deep); }

  .fruit--cherry { background: radial-gradient(circle, rgba(201,162,107,.55), rgba(201,162,107,0)); }
  .fruit--apple { background: radial-gradient(circle, rgba(184,132,76,.45), rgba(184,132,76,0)); }

  .floor-sketch { position: absolute; width: 56px; height: 56px; border-radius: 50%;
    background: radial-gradient(circle, rgba(60,60,60,.18), rgba(60,60,60,0)); }
  .floor-sketch--cherry { left: 14px; top: 1035px; }
  .floor-sketch--apple { left: 556px; top: 1040px; }

  /* large presentation label */
  .feature-label {
    position: absolute; left: 550px; top: 40px; width: 290px;
    display: flex; flex-direction: column; align-items: center; text-align: center;
  }
  .feature-label__tagline { font-size: 10px; letter-spacing: 2.5px; color: var(--gold); font-weight: 700; text-transform: uppercase; white-space: nowrap; }
  .feature-label__seal {
    margin-top: 42px; width: 280px; height: 280px; border-radius: 50%;
    border: 3px solid var(--ink);
    display: flex; flex-direction: column; align-items: center; justify-content: center; gap: 16px;
  }
  .feature-label__name { font-weight: 700; font-size: 38px; letter-spacing: 2px; color: var(--ink-soft); text-transform: uppercase; }
  .feature-label__met { font-weight: 700; font-size: 16px; letter-spacing: 1px; color: var(--ink-soft); }
  .feature-label__origin { font-weight: 700; font-size: 10px; letter-spacing: 1px; color: var(--ink-soft); text-transform: uppercase; white-space: nowrap; }
  .feature-label__variety { margin-top: 40px; font-weight: 700; font-size: 18px; letter-spacing: 5px; color: var(--gold); }
  .feature-label__year { font-family: "Playfair Display", serif; font-style: italic; font-size: 26px; color: var(--gold); margin-top: 18px; }
  .feature-label__fruit { width: 84px; height: 96px; border-radius: 50%; margin-top: 40px;
    background: radial-gradient(circle, rgba(201,162,107,.45), rgba(201,162,107,0)); }
  .feature-label__sweetness { font-family: "Cormorant Garamond", serif; font-size: 22px; color: var(--gold-deep); margin-top: 40px; letter-spacing: 1px; }

  /* mono label variant */
  .mono-label {
    position: absolute; left: 570px; top: 775px; width: 250px; height: 250px;
    border-radius: 50%; background: #fff; border: 3px solid var(--ink);
    display: flex; flex-direction: column; align-items: center; justify-content: center; gap: 14px; text-align: center;
  }
  .mono-label__brand { display: flex; align-items: center; gap: 8px; }
  .mono-label__name { font-weight: 700; font-size: 32px; letter-spacing: 2px; color: var(--ink); text-transform: uppercase; }
  .mono-label__ring { width: 14px; height: 14px; border-radius: 50%; border: 2px solid var(--ink); }
  .mono-label__met { font-weight: 700; font-size: 13px; color: var(--ink); }
  .mono-label__origin { font-weight: 700; font-size: 9px; letter-spacing: 1.2px; color: var(--ink); text-transform: uppercase; white-space: nowrap; }
</style>
</head>
<body>

  <div class="closure-seal">
    <div class="closure-seal__face">
      <span class="closure-seal__name">TARQUIL</span>
      <span class="closure-seal__ring"></span>
    </div>
  </div>

  <section class="label-panel label-panel--cherry">
    <div class="neck-band">
      <span class="neck-band__ring"></span>
      <span class="neck-band__name">TARQUIL</span>
    </div>
    <div class="label-body">
      <p class="label-body__tagline">Honigwein · 100% Naturprodukt</p>
      <div class="label-body__brand">
        <span class="label-body__name">Tarquil</span>
        <span class="label-body__ring"></span>
      </div>
      <p class="label-body__met">MET</p>
      <p class="label-body__origin">Qualität aus dem Schwarzwald</p>
      <p class="label-body__variety">KIRSCH-MET</p>
      <p class="label-body__year">2022</p>
      <div class="label-body__fruit fruit--cherry" role="img" aria-label="Gezeichnete Kirschen in Gold"></div>
      <p class="label-body__sweetness">-halbtrocken-</p>
    </div>
  </section>

  <section class="label-panel label-panel--apple">
    <div class="neck-band">
      <span class="neck-band__ring"></span>
      <span class="neck-band__name">TARQUIL</span>
    </div>
    <div class="label-body">
      <p class="label-body__tagline">Honigwein · 100% Naturprodukt</p>
      <div class="label-body__brand">
        <span class="label-body__name">Tarquil</span>
        <span class="label-body__ring"></span>
      </div>
      <p class="label-body__met">MET</p>
      <p class="label-body__origin">Qualität aus dem Schwarzwald</p>
      <p class="label-body__variety">APFEL-MET</p>
      <p class="label-body__year">2022</p>
      <div class="label-body__fruit fruit--apple" role="img" aria-label="Gezeichneter Apfel in Gold"></div>
      <p class="label-body__sweetness">-halbtrocken-</p>
    </div>
  </section>

  <div class="floor-sketch floor-sketch--cherry" role="img" aria-label="Skizze von Kirschen"></div>
  <div class="floor-sketch floor-sketch--apple" role="img" aria-label="Skizze eines Apfels"></div>

  <section class="feature-label">
    <p class="feature-label__tagline">Honigwein · 100% Naturprodukt</p>
    <div class="feature-label__seal">
      <span class="feature-label__name">Tarquil</span>
      <p class="feature-label__met">MET</p>
      <p class="feature-label__origin">Qualität aus dem Schwarzwald</p>
    </div>
    <p class="feature-label__variety">APFEL-MET</p>
    <p class="feature-label__year">2022</p>
    <div class="feature-label__fruit" role="img" aria-label="Gezeichneter Apfel in Gold"></div>
    <p class="feature-label__sweetness">-halbtrocken-</p>
  </section>

  <section class="mono-label">
    <div class="mono-label__brand">
      <span class="mono-label__name">Tarquil</span>
      <span class="mono-label__ring"></span>
    </div>
    <p class="mono-label__met">MET</p>
    <p class="mono-label__origin">Qualität aus dem Schwarzwald</p>
  </section>

</body>
</html>
```